Security based company delivering High Risk Training to Law Enforcement Agencies Worldwide.

We need a Web design for a company doing business in Washington D.C. We deliver High Risk Training to Law Enforcement Agencies throughout the world. Our focus is on Improvised Explosive Devices. We train Bomb Technicians and First Responders in all aspects relating to bombings and criminal incidents globally.
Updates

Reason: We have uploaded our logo. Thank you.

Target Market(s)

Military and Law Enforcement Personnel from around the world.

Industry/Entity Type

Business

Requirements
Should not have
• Do not include cartoon like characters.

```html
<!DOCTYPE html>
<html lang="en">
<head>
<meta charset="utf-8">
<title>Vantrex International</title>
<link href="https://fonts.googleapis.com/css2?family=Arimo:wght@400;700&display=swap" rel="stylesheet">
<style>
:root{
  --red:#d71920;
  --red-dark:#a80f14;
  --ink:#333333;
  --muted:#555555;
  --line:#dddddd;
  --page:#ffffff;
  --footer:#2b2b2b;
  --footer-bar:#1e1e1e;
  --footer-text:#bbbbbb;
  --btn:#3a3a3a;
}
*{box-sizing:border-box;margin:0;padding:0}
html,body{width:667px;height:1200px;overflow:hidden;background:var(--page)}
body{position:relative;font-family:"Arimo",Arial,sans-serif;color:var(--ink);font-size:8px;line-height:1.45}
h1,h2,h3,h4,h5{font-weight:400}
.abs{position:absolute}
.top-rule{left:0;top:0;width:667px;height:3px;background:var(--red)}
.brand{left:77px;top:18px;display:flex;align-items:center;gap:8px}
.brand-mark{width:36px;height:36px;border-radius:50%;background:var(--red)}
.brand-name{font-weight:700;font-size:22px;color:#222;letter-spacing:.5px;line-height:1}
.brand-name small{display:block;font-size:8px;letter-spacing:2px;margin-top:3px}
.search{left:437px;top:12px;width:153px;height:17px;border:1px solid var(--line);border-radius:2px;font-size:7px;color:#aaa;padding:3px 6px}
.search svg{position:absolute;right:5px;top:3px}
.account{left:516px;top:46px;font-size:10px;color:#222}
.account span{margin:0 6px}
.nav{left:77px;top:73px;width:513px;height:23px;background:var(--red);display:flex;align-items:center;font-size:6.6px;font-weight:700;color:#fff;border-radius:2px 2px 0 0;overflow:hidden}
.nav a{flex:1 1 auto;padding:0 3px;color:#fff;text-decoration:none;line-height:23px;white-space:nowrap;text-align:center}
.nav a.active{background:#222;flex:0 0 auto;padding:0 9px}
.hero{left:0;top:96px;width:667px;height:229px;background:linear-gradient(180deg,#b9ac98 0%,#8f8271 45%,#c7b8a2 100%)}
.hero-caption{left:338px;top:157px;width:252px;height:105px;background:rgba(40,40,40,.82);border-radius:3px;padding:10px 10px;color:#eee}
.hero-caption h2{font-size:13px;font-weight:700;color:#fff;margin-bottom:5px}
.hero-caption h2 em{font-style:normal;color:var(--red)}
.hero-caption p{font-size:7.5px;line-height:1.5}
.hero-arrow{top:212px;width:22px;height:22px;background:#333;display:flex;align-items:center;justify-content:center}
.dots{display:flex;gap:5px}
.dots i{width:8px;height:8px;border-radius:50%;background:#fff;display:block}
.dots i.on{background:var(--red)}
.welcome{left:77px;top:325px;width:513px;height:106px;background:#fff;border-radius:3px;text-align:center;padding:9px 10px}
.welcome h1{font-size:14px;color:#333;margin-bottom:6px}
.welcome h1 em,.section-title em{font-style:normal;color:var(--red)}
.welcome p{font-size:7.5px;color:var(--muted)}
.btn{display:inline-block;background:var(--btn);color:#fff;font-size:7px;padding:3px 7px;border-radius:2px}
.btn.red{background:var(--red)}
.divider{left:77px;width:513px;height:1px;background:var(--line)}
.section-title{left:77px;width:513px;text-align:center;font-size:14px;color:#444}
.pager{display:flex;gap:4px}
.pager b{width:15px;height:15px;background:#333;display:flex;align-items:center;justify-content:center}
.pager b.red{background:var(--red)}
.card{top:477px;width:119px;height:164px;border:1px solid var(--line);border-radius:3px;text-align:center;overflow:hidden}
.card .photo{height:78px}
.card h3{font-size:9.5px;color:var(--red);margin:4px 0 3px}
.card p{font-size:7.5px;color:var(--muted);text-align:left;padding:0 8px;margin-bottom:6px}
.video{left:77px;top:693px;width:260px;height:168px;border:1px solid var(--line);padding:4px}
.video .photo{height:146px;background:linear-gradient(160deg,#c9b8a2,#8a7b68 60%,#d89a40)}
.video .bar{height:12px;background:#222;margin-top:1px;display:flex;align-items:center;padding:0 6px;gap:5px}
.video .track{flex:1;height:3px;background:#555;position:relative}
.video .track i{position:absolute;left:0;top:0;width:48%;height:3px;background:var(--red)}
.post{left:353px;width:237px;height:52px}
.post .thumb{position:absolute;left:0;top:0;width:87px;height:46px;border:1px solid var(--line);padding:2px}
.post .thumb div{width:100%;height:100%}
.post .txt{position:absolute;left:98px;top:0;width:139px}
.post h4{font-size:8.5px;font-weight:700;color:var(--red);line-height:1.2}
.post p{font-size:7.5px;color:var(--muted);text-align:justify;line-height:1.3}
.post strong{font-size:7px;color:#222}
.avatar{left:77px;top:911px;width:56px;height:56px;border-radius:50%;border:2px solid var(--red);padding:3px}
.avatar div{width:100%;height:100%;border-radius:50%;background:linear-gradient(#c9a98a,#8a6a55)}
.quote{left:140px;top:920px;width:450px;text-align:center;font-size:7.5px;color:var(--muted)}
.quote .who{color:var(--red);font-weight:700;font-size:7px;margin-top:7px}
.quote .who span{color:#222}
.tdots i{background:#ccc}
.footer{left:0;width:667px;background:var(--footer);border-top:4px solid var(--red)}
.fcol{top:1027px;color:var(--footer-text);font-size:7.5px}
.fcol h5{font-size:10px;color:var(--red);margin-bottom:5px}
.fcol li{list-style:none;line-height:1.45}
.fcol.links li::before{content:"›";color:var(--red);margin-right:5px}
.fcol.news li{display:flex;gap:5px;margin-bottom:12px;line-height:1.4}
.fcol.news li::before{content:"›";color:var(--red)}
.fcol.social li{display:flex;align-items:center;gap:9px;margin-bottom:11px}
.fcol.social li i{width:15px;height:15px;border-radius:50%;background:#555;display:block}
.footer-bar{left:0;top:1170px;width:667px;height:30px;background:var(--footer-bar);color:#aaa;font-size:7px;text-align:center;line-height:30px}
</style>
</head>
<body>
<div class="abs top-rule"></div>

<header>
  <div class="abs brand"><span class="brand-mark"></span><div class="brand-name">VANTREX<small>INTERNATIONAL</small></div></div>
  <div class="abs search">Search..
    <svg width="9" height="9" viewBox="0 0 10 10"><circle cx="4" cy="4" r="3" fill="none" stroke="#d71920" stroke-width="1.5"/><line x1="6.3" y1="6.3" x2="9" y2="9" stroke="#d71920" stroke-width="1.5"/></svg>
  </div>
  <div class="abs account">Login<span>|</span>Sign Up</div>
  <nav class="abs nav">
    <a class="active">Home</a><a>About Us</a><a>Lorem Ipsum</a><a>Consectetuer</a><a>Adipiscing Elit</a><a>Nostrud Exerci Tation</a><a>Consectetuer Adipiscing</a><a>Tation Ullamco</a>
  </nav>
</header>

<section>
  <div class="abs hero" role="img" aria-label="Controlled explosion training beside a white car in a desert range"></div>
  <div class="abs hero-caption">
    <h2><em>Consectetuer</em> Adipiscing Elit</h2>
    <p>Lorem ipsum dolor sit amet, consectetuer adipiscing elit, sed diam nonummy nibh euismod tincidunt ut laoreet dolore magna aliquam erat volutpat. Ut wisi enim ad minim veniam, quis nostrud exerci tation ullamcorper suscipit lobortis nisl ut aliquip ex ea commodo consequat. Duis autem vel eum iriure dolor in hendrerit.</p>
  </div>
  <div class="abs hero-arrow" style="left:0"><svg width="8" height="10"><path d="M7 0 L1 5 L7 10Z" fill="#fff"/></svg></div>
  <div class="abs hero-arrow" style="left:645px"><svg width="8" height="10"><path d="M1 0 L7 5 L1 10Z" fill="#fff"/></svg></div>
  <div class="abs dots" style="left:309px;top:300px"><i></i><i></i><i class="on"></i><i></i></div>
</section>

<section class="abs welcome">
  <h1>Welcome to <em>Vantrex International</em></h1>
  <p>Lorem ipsum dolor sit amet, consectetuer adipiscing elit, sed diam nonummy nibh euismod tincidunt ut laoreet dolore magna aliquam erat volutpat. Ut wisi enim ad minim veniam, quis nostrud exerci tation ullamcorper suscipit lobortis nisl ut aliquip ex ea commodo consequat. Duis autem vel eum iriure dolor in hendrerit in vulputate velit esse molestie consequat, vel illum dolore eu feugiat nulla facilisis at vero eros et accumsan et iusto odio dignissim qui blandit praesent luptatum zzril delenit augue duis dolore te feugait nulla facilisi.</p>
  <span class="btn" style="margin-top:8px">Read More</span>
</section>

<div class="abs divider" style="top:440px"></div>
<h2 class="abs section-title" style="top:447px">Vantrex International <em>Services</em></h2>
<div class="abs pager" style="left:554px;top:447px"><b><svg width="5" height="7"><path d="M5 0 L0 3.5 L5 7Z" fill="#fff"/></svg></b><b class="red"><svg width="5" height="7"><path d="M0 0 L5 3.5 L0 7Z" fill="#fff"/></svg></b></div>

<article class="abs card" style="left:77px"><div class="photo" role="img" aria-label="Car engulfed in a training blast" style="background:linear-gradient(120deg,#d8d4cc,#e8a040)"></div><h3>Consectetuer adipiscing</h3><p>Lorem ipsum dolor sit amet, consectetuer adipiscing elit, sed diam nonummy nibh.</p><span class="btn">Read More</span></article>
<article class="abs card" style="left:208px"><div class="photo" role="img" aria-label="Debris thrown up from sandy ground" style="background:linear-gradient(160deg,#d9c9ad,#b09878)"></div><h3>Consectetuer adipiscing</h3><p>Lorem ipsum dolor sit amet, consectetuer adipiscing elit, sed diam nonummy nibh.</p><span class="btn red">Read More</span></article>
<article class="abs card" style="left:340px"><div class="photo" role="img" aria-label="Technician in a bomb disposal suit" style="background:linear-gradient(160deg,#a9b29a,#6d7358)"></div><h3>Consectetuer adipiscing</h3><p>Lorem ipsum dolor sit amet, consectetuer adipiscing elit, sed diam nonummy nibh.</p><span class="btn">Read More</span></article>
<article class="abs card" style="left:471px"><div class="photo" role="img" aria-label="Bomb technician approaching a device on an airfield" style="background:linear-gradient(180deg,#c8ccd2,#a49e94)"></div><h3>Consectetuer adipiscing</h3><p>Lorem ipsum dolor sit amet, consectetuer adipiscing elit, sed diam nonummy nibh.</p><span class="btn">Read More</span></article>

<div class="abs divider" style="top:657px"></div>
<h2 class="abs section-title" style="top:666px">Video <em>Blog</em></h2>
<div class="abs pager" style="left:554px;top:668px"><b><svg width="5" height="7"><path d="M5 0 L0 3.5 L5 7Z" fill="#fff"/></svg></b><b class="red"><svg width="5" height="7"><path d="M0 0 L5 3.5 L0 7Z" fill="#fff"/></svg></b></div>

<div class="abs video">
  <div class="photo" role="img" aria-label="Video still of a car burning after a controlled blast"></div>
  <div class="bar"><svg width="6" height="7"><path d="M0 0 L6 3.5 L0 7Z" fill="#fff"/></svg><div class="track"><i></i></div><svg width="8" height="7"><rect width="8" height="7" fill="none" stroke="#fff"/></svg></div>
</div>

<article class="abs post" style="top:695px"><div class="thumb"><div role="img" aria-label="Car in a training blast" style="background:linear-gradient(120deg,#d8d4cc,#e8a040)"></div></div><div class="txt"><h4>Consectetuer Adipiscing elit</h4><p>Lorem ipsum dolor sit amet, consectetuer adipiscing elit, sed diam nonummy nibh euismod tincidunt ut laoreet.</p><strong>Read More</strong></div></article>
<article class="abs post" style="top:756px"><div class="thumb"><div role="img" aria-label="Technician on an airfield range" style="background:linear-gradient(180deg,#c8ccd2,#a49e94)"></div></div><div class="txt"><h4>Consectetuer Adipiscing elit</h4><p>Lorem ipsum dolor sit amet, consectetuer adipiscing elit, sed diam nonummy nibh euismod tincidunt ut laoreet.</p><strong>Read More</strong></div></article>
<article class="abs post" style="top:817px"><div class="thumb"><div role="img" aria-label="Technician in protective suit" style="background:linear-gradient(160deg,#a9b29a,#6d7358)"></div></div><div class="txt"><h4>Consectetuer Adipiscing elit</h4><p>Lorem ipsum dolor sit amet, consectetuer adipiscing elit, sed diam nonummy nibh euismod tincidunt ut laoreet.</p><strong>Read More</strong></div></article>

<div class="abs divider" style="top:881px"></div>
<h2 class="abs section-title" style="top:888px">Client <em>Testimonials</em></h2>
<div class="abs avatar"><div role="img" aria-label="Client portrait"></div></div>
<blockquote class="abs quote">
  <p>“ Lorem ipsum dolor sit amet, consectetuer adipiscing elit, sed diam nonummy nibh euismod tincidunt ut laoreet dolore magna aliquam erat volutpat. Ut wisi enim ad minim veniam, quis nostrud exerci tation ullamcorper suscipit lobortis nisl ut aliquip ex ea commodo consequat. Duis autem vel eum iriure dolor in hendrerit in vulputate velit esse molestie consequat ”</p>
  <p class="who">Quis nostrud exerci Tation, <span>Aus</span></p>
</blockquote>
<div class="abs dots tdots" style="left:309px;top:984px"><i></i><i class="on" style="background:var(--red)"></i><i></i><i></i></div>
<div class="abs divider" style="top:1002px"></div>

<footer>
  <div class="abs footer" style="top:1012px;height:158px"></div>
  <div class="abs fcol links" style="left:77px"><h5>Main Links</h5><ul><li>Home</li><li>About Us</li><li>Lorem Ipsum</li><li>Consectetuer</li><li>Adipiscing Elit</li><li>Nostrud Exerci Tation</li><li>Consectetuer Adipiscing</li><li>Tation Ullamco</li></ul></div>
  <div class="abs fcol links" style="left:217px"><h5>Categories</h5><ul><li>Lorem ipsum dolo</li><li>consectetuer adipiscing</li><li>Lorem Ipsum</li><li>Quis nostrud exerci tation</li><li>Adipiscing Elit</li><li>Nostrud Exerci Tation</li><li>Consectetuer Adipiscing</li><li>Eum iriure dolor in hendrerit</li></ul></div>
  <div class="abs fcol news" style="left:352px;width:135px"><h5>News &amp; Events</h5><ul><li>Lorem ipsum dolor sit amet, consectetuer adipiscing elit, sed diam nonummy nibh euismod tincidunt.</li><li>Lorem ipsum dolor sit amet, consectetuer adipiscing elit, sed diam nonummy nibh euismod tincidunt.</li><li>Lorem ipsum dolor sit amet, consectetuer adipiscing elit, sed diam nonummy nibh euismod tincidunt.</li></ul></div>
  <div class="abs fcol social" style="left:527px"><h5>Follow Us On</h5><ul><li><i></i>network</li><li><i></i>updates</li><li><i></i>circles</li><li><i></i>videos</li></ul></div>
  <div class="abs footer-bar">© 2014 Vantrex International. All Rights Reserved.</div>
</footer>
</body>
</html>
```